Ferncastle Holdings - stationery for luxury, exclusive property investment company

We need stationery (letterhead, folder, compliments slip and envelope) and business cards which will reflect our luxury brand.

I have attached some design examples that we like.

We are an investment company which buys property to provide accommodation for corporate customers.

The design of the stationery needs to be be simple, refined, understated, luxury and very tasteful.

The design should communicate luxury and exclusivity, without being ostentatious.

Logo files are attached

Please can designers re-read the brief, and make sure the logo is in gold on either on a navy or white background.

Target Market(s)

Wealthy customers

Contact Information for Business Card

Helen Travers-Booth
Director
Ferncastle Holdings Limited
email: helen@ferncastleholdings.co.uk
mob: 07712645930

Font styles to use
Serif

Colors

Designer to choose colors to be used in the design.

Requirements
Must have
• The logo must be gold on either a white or navy background as per the attached logos.
• The stationery MUST have the following information:
• Ferncastle Holdings Limited
• The Willows
• Ashby Rise
• Ashby
• GL52 7TN
• Company Number: 20418736 (Registered in England and Wales)
• The letterhead must also have the two attached logos for the PLG and the PLG accreditation scheme. They do not need to be large.
Nice to have
• A watermark, navy banding either top or bottom.
Should not have
• Anything that looks budget.

```html
<!DOCTYPE html>
<html lang="en">
<head>
<meta charset="utf-8">
<title>Ferncastle Holdings – Presentation Folder</title>
<link rel="stylesheet" href="https://fonts.googleapis.com/css2?family=Cinzel:wght@500&display=swap">
<style>
  :root {
    --navy: #27285a;
    --navy-deep: #1f2050;
    --navy-soft: #303268;
    --gold: #c9a24e;
    --gold-light: #f4dfa2;
    --gold-mid: #dcaa45;
    --gold-dark: #c08a2c;
    --backdrop: #ffffff;
    --crease: #1a1b44;
  }
  * { margin: 0; padding: 0; box-sizing: border-box; }
  html, body {
    width: 1200px; height: 1000px; overflow: hidden;
    background: var(--backdrop);
    font-family: "Cinzel", "Times New Roman", serif;
  }
  .sheet {
    position: relative; width: 1200px; height: 1000px;
    display: flex; align-items: center; justify-content: center; gap: 40px;
  }
  .panel {
    position: relative; width: 360px; height: 510px;
    background: var(--navy); overflow: hidden;
    box-shadow: 0 2px 6px rgba(0,0,0,.18);
  }
  .front-cover {
    background: radial-gradient(ellipse at 40% 35%, var(--navy-soft), var(--navy-deep) 80%);
  }
  .cover-watermark {
    position: absolute; left: -80px; top: 30px;
    width: 420px; height: 420px; border-radius: 50%;
    border: 26px solid rgba(255,255,255,.035);
  }
  .lockup {
    position: absolute; left: 0; right: 0;
    display: flex; flex-direction: column; align-items: center;
    color: var(--gold); font-weight: 500; text-align: center;
  }
  .cover-lockup { top: 185px; }
  .lockup-mark {
    width: 46px; height: 46px; border-radius: 50%;
    border: 2px solid var(--gold); margin-bottom: 18px;
  }
  .lockup-name { font-size: 33px; letter-spacing: .5px; line-height: 1; }
  .lockup-sub { font-size: 16px; letter-spacing: 7px; margin-top: 8px; }
  .inside-spread {
    display: flex; width: 720px; height: 510px;
    box-shadow: 0 2px 6px rgba(0,0,0,.18);
  }
  .inside-spread .panel { box-shadow: none; }
  .inside-left { border-right: 2px solid var(--crease); }
  .inside-pattern {
    position: absolute; inset: 0; background: var(--navy);
  }
  .pocket {
    position: absolute; left: 0; right: 0; bottom: 0; height: 205px;
    background: radial-gradient(ellipse at 50% 45%, var(--gold-light) 0%, var(--gold-mid) 55%, var(--gold-dark) 100%);
  }
  .pocket-left { clip-path: polygon(0 10%, 100% 0, 100% 100%, 0 100%); }
  .pocket-right { clip-path: polygon(0 0, 100% 8%, 100% 100%, 0 100%); }
  .pocket-lockup { top: 70px; color: var(--navy); }
  .pocket-lockup .lockup-mark {
    width: 26px; height: 26px; border-color: var(--navy); margin-bottom: 8px;
  }
  .pocket-lockup .lockup-name { font-size: 20px; }
  .pocket-lockup .lockup-sub { font-size: 10px; letter-spacing: 4px; margin-top: 4px; }
  .card-slot {
    position: absolute; left: 50%; top: 88px; transform: translateX(-50%);
    width: 96px; height: 60px; border-radius: 8px;
    background: var(--navy);
    box-shadow: inset 0 2px 4px rgba(0,0,0,.5);
  }
</style>
</head>
<body>
  <main class="sheet">
    <section class="panel front-cover">
      <div class="cover-watermark" aria-hidden="true"></div>
      <div class="lockup cover-lockup">
        <span class="lockup-mark" aria-hidden="true"></span>
        <span class="lockup-name">FERNCASTLE</span>
        <span class="lockup-sub">HOLDINGS</span>
      </div>
    </section>

    <section class="inside-spread">
      <div class="panel inside-left">
        <div class="inside-pattern" role="img" aria-label="Tone-on-tone navy repeat pattern of the company monogram"></div>
        <div class="pocket pocket-left">
          <div class="lockup pocket-lockup">
            <span class="lockup-mark" aria-hidden="true"></span>
            <span class="lockup-name">FERNCASTLE</span>
            <span class="lockup-sub">HOLDINGS</span>
          </div>
        </div>
      </div>
      <div class="panel inside-right">
        <div class="inside-pattern" role="img" aria-label="Tone-on-tone navy repeat pattern of the company monogram"></div>
        <div class="pocket pocket-right">
          <div class="card-slot" aria-label="Business card slot"></div>
        </div>
      </div>
    </section>
  </main>
</body>
</html>
```